Modern Catering Company needs Letterhead Design

We need a letterhead design that will make effective use of the corporate logo and color scheme, along with careful typography, helps this letterhead design communicate the brand well. We do have a corporate logo, however feel free to enhance the color scheme with gold and purple. We are serving a very upscale clientele so the letterhead has to reflect elegance, professionalism, cleanliness, and modern style. We are branding the company so the letterhead and business cards must fit the brand story. There should be no cartoonish elements in the design and we are looking for sharper lines.

Target Market(s)

Businesses and upscale clientele

Industry/Entity Type

Catering

Contact Information for Business Card

while this design can have any number of quirks and distinctions, it needs to be cohesive with the entire brand story clean, professional but edgy

Requirements
Must have
• must have good and carefully placement of it’s logo and where you place the text or the message. Colors blue, very deep purple, jewel tones not pastels, gold. Blue must be the primary color you may accent with purple or gold. Contact information is as follows: Co-Owners/ Chefs: R. Hollowmere & L. Brandt, phone: 414-555-0182 email:Contact@orchardtablecatering.example, address: 6127 W Larkspur Hollow Rd, Milwaukee, WI 53299
Should not have
• pastel colors, Do not add the BBQ information to the letterhead or business card it was a mistake by the previous designer.

```html
<!DOCTYPE html>
<html lang="en">
<head>
<meta charset="utf-8">
<title>Orchard Table Catering Letterhead</title>
<link href="https://fonts.googleapis.com/css2?family=Open+Sans:wght@400;600&display=swap" rel="stylesheet">
<style>
  :root {
    --backdrop: #e6e7e9;
    --paper: #ffffff;
    --brand-blue: #3d6ab3;
    --charcoal: #333333;
    --ink-light: #ffffff;
    --watermark: #eceef3;
  }
  * { box-sizing: border-box; margin: 0; padding: 0; }
  html, body {
    width: 1200px;
    height: 849px;
    overflow: hidden;
    background: var(--backdrop);
    font-family: "Open Sans", Arial, sans-serif;
  }
  .letterhead {
    position: absolute;
    left: 333px;
    top: 47px;
    width: 535px;
    height: 756px;
    background: var(--paper);
  }
  .letterhead-header {
    position: relative;
    width: 535px;
    height: 103px;
  }
  .header-bands {
    position: absolute;
    inset: 0;
  }
  .contact-block {
    position: absolute;
    left: 24px;
    top: 12px;
    color: var(--ink-light);
    font-size: 10.5px;
    line-height: 13px;
    letter-spacing: 0.3px;
  }
  .contact-address { margin-bottom: 7px; }
  .contact-line {
    display: flex;
    align-items: center;
    gap: 8px;
  }
  .contact-line svg { width: 9px; height: 9px; flex: none; }
  .brand-name {
    position: absolute;
    right: 22px;
    top: 28px;
    display: flex;
    align-items: center;
    gap: 8px;
    color: var(--ink-light);
    font-weight: 600;
    font-size: 13px;
    line-height: 16px;
    letter-spacing: 1.5px;
    text-transform: uppercase;
    text-align: right;
  }
  .brand-dot {
    width: 12px;
    height: 12px;
    border-radius: 50%;
    background: var(--ink-light);
    flex: none;
  }
  .page-watermark {
    position: absolute;
    left: 147px;
    top: 310px;
    width: 240px;
    height: 240px;
    border-radius: 50%;
    background: var(--watermark);
  }
</style>
</head>
<body>
  <article class="letterhead">
    <header class="letterhead-header">
      <svg class="header-bands" width="535" height="103" viewBox="0 0 535 103" aria-hidden="true">
        <rect x="0" y="0" width="535" height="103" fill="var(--charcoal)"/>
        <polygon points="0,0 348,0 302,66 7,103 0,103" fill="var(--brand-blue)"/>
        <polyline points="7,103 302,66 348,0" fill="none" stroke="var(--ink-light)" stroke-width="0.8"/>
      </svg>
      <div class="contact-block">
        <p class="contact-address">6127 W Larkspur Hollow Rd<br>Milwaukee, WI 53299</p>
        <p class="contact-line">
          <svg viewBox="0 0 10 10" aria-hidden="true"><path d="M2 1 L4 1 L4.6 3 L3.5 4 Q4.5 6 6 6.5 L7 5.4 L9 6 L9 8 Q8.5 9 7.5 9 Q1 8 1 2 Q1 1 2 1Z" fill="var(--ink-light)"/></svg>
          414-555-0182
        </p>
        <p class="contact-line">
          <svg viewBox="0 0 10 10" aria-hidden="true"><rect x="1" y="2.5" width="8" height="5.5" fill="none" stroke="var(--ink-light)" stroke-width="1"/><polyline points="1,2.5 5,5.5 9,2.5" fill="none" stroke="var(--ink-light)" stroke-width="1"/></svg>
          Contact@orchardtablecatering.example
        </p>
      </div>
      <div class="brand-name">
        <span class="brand-dot"></span>
        <span>Orchard Table<br>Catering</span>
      </div>
    </header>
    <div class="page-watermark" role="img" aria-label="Faint brand watermark"></div>
  </article>
</body>
</html>
```